International Wine events organiser seeks simple but stunning business card

I am a freelance events, marketing and PR provider specialised in the Wine industry. I help wineries and wine regions reach trade and consumers in foreign markets through events, help with the websites and communications, press trips and promotional activities. I am looking for a business card which is simple yet effective and is linked to events and communication.

I work mainly - but exclusively - with Italian wineries organising events for them in foreign market.s

I would like to use red in the logo as my present website (lunabrendor.com) used grey and red (although I will be changing the design at a later date).

Target Market(s)

Wine producers, promotional bodies in wine sector, companies looking to hire event organisers,

Industry/Entity Type

Marketing

Requirements
Must have
• My Name - Luna Brendor
My address
My phone
My website : www.lunabrendor.com
my Blog : pebbleandtwig.me

Should not have
• Butterflies, stars, flowers, anything not particularly linked to wine - would like to keep it simple, modern and eye-catching without being too cliche.

```html
<!DOCTYPE html>
<html lang="en">
<head>
<meta charset="utf-8">
<title>Luna Brendor – Business Card</title>
<link rel="stylesheet" href="https://fonts.googleapis.com/css2?family=Crimson+Text:ital,wght@1,400;1,700&display=swap">
<style>
  :root {
    --card-bg: #ffffff;
    --card-border: #3a3a3a;
    --wine: #7a1446;
    --ink: #1a1a1a;
    --vine-grey: #e4e4e4;
    --grape-light: rgba(176, 104, 138, 0.55);
    --grape-deep: rgba(140, 60, 95, 0.5);
  }
  * { margin: 0; padding: 0; box-sizing: border-box; }
  html, body {
    width: 1200px;
    height: 777px;
    overflow: hidden;
    background: var(--card-bg);
  }
  .card {
    position: relative;
    width: 1200px;
    height: 777px;
    background: var(--card-bg);
    border: 1px solid var(--card-border);
    overflow: hidden;
    font-family: "Crimson Text", "Palatino Linotype", serif;
    font-style: italic;
    color: var(--ink);
  }
  .vine-artwork {
    position: absolute;
    left: 0;
    top: 0;
    width: 700px;
    height: 777px;
    background: linear-gradient(to right,
      var(--grape-light) 0%,
      var(--grape-deep) 18%,
      var(--vine-grey) 42%,
      rgba(228, 228, 228, 0.6) 70%,
      rgba(255, 255, 255, 0) 100%);
    opacity: 0.75;
  }
  .details {
    position: absolute;
    left: 538px;
    top: 0;
    right: 0;
    bottom: 0;
  }
  .line {
    position: absolute;
    left: 0;
    white-space: nowrap;
    font-size: 44px;
    line-height: 1;
  }
  .name {
    top: 68px;
    font-size: 49px;
    font-weight: 700;
    color: var(--wine);
    letter-spacing: 0.5px;
  }
  .street  { top: 261px; }
  .city    { top: 323px; }
  .phone   { top: 414px; }
  .email   { top: 476px; }
  .website { top: 607px; font-weight: 700; }
  .blog    { top: 670px; }
</style>
</head>
<body>
  <div class="card">
    <div class="vine-artwork" role="img" aria-label="Soft illustration of a grey vine leaf with a cluster of translucent wine-red grapes"></div>
    <div class="details">
      <div class="line name">Luna Brendor</div>
      <div class="line street">Kastanienweg 12</div>
      <div class="line city">80469 Munich</div>
      <div class="line phone">Phone +49 1705552318</div>
      <div class="line email">luna@lunabrendor.com</div>
      <div class="line website">www.lunabrendor.com</div>
      <div class="line blog">Blog: pebbleandtwig.me</div>
    </div>
  </div>
</body>
</html>
```